Solar energy proposal for homeowners

I am providing households with solar energy proposals, and I need a high-quality brochure that is packaged cleverly to attract the homeowner's attention. Take a look at the one page solar brochure that I have included to get an idea of text and content.

Target Market(s)

Residential Homeowners

Industry/Entity Type

Solar

Requirements
Must have
• High quality document

```html
<!DOCTYPE html>
<html lang="en">
<head>
<meta charset="utf-8">
<title>Brightvale Energy – Solar Flyers</title>
<link href="https://fonts.googleapis.com/css2?family=Roboto:wght@300;400;500;700&display=swap" rel="stylesheet">
<style>
  :root{
    --backdrop:#d1d2d4;
    --navy:#384772;
    --lime:#b2d235;
    --teal:#2aa9c9;
    --brand-text:#7cc9a4;
    --sky-top:#5b8fc4;
    --panel-blue:#2f4f96;
    --ink:#1d1d1d;
    --paper:#ffffff;
    --panel-grey:#f3f4f6;
  }
  *{box-sizing:border-box;margin:0;padding:0}
  html,body{width:1200px;height:1097px;overflow:hidden}
  body{background:var(--backdrop);font-family:"Roboto",Arial,sans-serif;position:relative}

  .flyer{position:absolute;width:537px;height:695px;background:var(--paper);overflow:hidden}
  .flyer--front{left:52px;top:171px}
  .flyer--back{left:627px;top:230px}

  .sky-strip{position:absolute;left:0;top:0;width:100%;height:18px;background:linear-gradient(90deg,var(--sky-top),#8fb8d8 60%,#c4dce8)}
  .header-band{position:absolute;left:0;top:18px;width:100%;height:95px;background:var(--navy)}

  .brand{position:absolute;left:36px;top:50px;display:flex;align-items:center;gap:10px}
  .brand__mark{width:28px;height:28px;background:var(--teal);flex:none}
  .brand__name{font-family:"Roboto",Arial,sans-serif;font-weight:300;font-size:22px;color:var(--brand-text);letter-spacing:.3px;line-height:1;white-space:nowrap}

  /* Front */
  .hero-photo{position:absolute;left:0;top:113px;width:100%;height:319px;
    background:linear-gradient(180deg,#a9d3df 0%,#cfe4e6 30%,#8fb4d0 52%,#3c5ea6 68%,var(--panel-blue) 100%);
    clip-path:polygon(0 0,100% 0,100% 100%,0 94.7%)}
  .hero-band{position:absolute;left:0;top:142px;width:400px;height:110px;background:rgba(255,255,255,.22)}
  .hero-title{position:absolute;left:38px;top:146px;color:#fff;font-weight:700;font-size:29px;line-height:34px;letter-spacing:.2px}
  .hero-tagline{position:absolute;left:38px;top:314px;color:#fff;font-weight:700;font-size:28px;line-height:34px}
  .chevron{position:absolute;left:0;top:0;width:537px;height:432px}

  .about{position:absolute;left:47px;top:461px;width:460px}
  .about__title{font-size:17px;font-weight:700;color:var(--navy)}
  .about__text{margin-top:16px;font-size:11.2px;line-height:13.8px;color:var(--ink)}
  .about__rule{position:absolute;left:47px;top:570px;width:111px;height:2px;background:var(--lime)}
  .call-now{position:absolute;left:47px;top:593px;font-size:21px;font-weight:700;color:var(--navy)}
  .front-footer{position:absolute;left:0;bottom:0;width:100%;height:60px;background:var(--navy);clip-path:polygon(0 0,100% 95%,100% 100%,0 100%)}

  /* Back */
  .section-title-top{position:absolute;left:281px;top:56px;color:#fff;font-weight:700;font-size:22px}
  .worker-photo{position:absolute;left:0;top:113px;width:100%;height:160px;
    background:linear-gradient(100deg,#8d949a 0%,#5e6670 35%,#9aa7b3 65%,#cfd9e2 100%)}
  .benefits{position:absolute;left:0;top:268px;width:100%;height:145px;
    background:linear-gradient(90deg,#8fae3e 0%,#9fc64a 50%,#a9d055 100%);
    clip-path:polygon(0 0,100% 0,100% 100%,0 88%)}
  .benefit{position:absolute;display:flex;align-items:center;gap:14px;color:#fff;font-weight:700;font-size:14px;white-space:nowrap}
  .benefit__mark{width:12px;height:12px;background:#fff}
  .benefit-rule{position:absolute;height:1px;background:rgba(255,255,255,.6)}

  .service-panel{position:absolute;left:268px;top:405px;width:241px;height:232px;background:var(--panel-grey)}
  .service-title{position:absolute;left:40px;top:416px;font-size:18px;font-weight:700;color:var(--navy)}
  .service{position:absolute}
  .service--left{width:174px}
  .service--right{width:194px}
  .service__icon{position:absolute;left:-33px;top:-2px;width:22px;height:24px}
  .service__name{font-size:12.5px;font-weight:700;color:var(--navy);white-space:nowrap}
  .service__text{margin-top:13px;font-size:10.2px;line-height:12.5px;color:var(--ink)}

  .back-footer{position:absolute;left:0;top:629px;width:100%;height:66px;background:var(--navy);clip-path:polygon(0 0,100% 16%,100% 100%,0 100%)}
  .cta{position:absolute;left:36px;top:637px;color:#fff;font-weight:700;font-size:15px}
  .contact-line{position:absolute;left:36px;top:666px;color:#fff;font-weight:700;font-size:9.3px;white-space:nowrap}
  .contact-line span{margin:0 10px}
</style>
</head>
<body>

<section class="flyer flyer--front">
  <div class="sky-strip"></div>
  <div class="header-band"></div>
  <div class="brand"><div class="brand__mark"></div><div class="brand__name">brightvale energy</div></div>

  <div class="hero-photo" role="img" aria-label="Rooftop solar panels under a bright cloudy sky"></div>
  <div class="hero-band"></div>
  <svg class="chevron" viewBox="0 0 537 432" aria-hidden="true">
    <polyline points="486,62 406,186 484,312" fill="none" stroke="#b2d235" stroke-width="70" stroke-linecap="round" stroke-linejoin="round"/>
  </svg>
  <h1 class="hero-title">SOLAR FOR $0 DOWN.<br>NO LIENS.<br>NO KIDDING.</h1>
  <p class="hero-tagline">POWER YOUR FUTURE WITH<br>BRIGHTVALE ENERGY!</p>

  <div class="about">
    <h2 class="about__title">ABOUT US</h2>
    <p class="about__text">At Brightvale Energy, our mission is to make solar simple and accessible for everyone. No high-pressure sales—just the information you need to make a smart choice. With our solar rental program, you can lower your monthly energy costs and pay less than your current electricity bill.</p>
  </div>
  <div class="about__rule"></div>
  <p class="call-now">Call Now! (555) 014-2290</p>
  <div class="front-footer"></div>
</section>

<section class="flyer flyer--back">
  <div class="sky-strip"></div>
  <div class="header-band"></div>
  <div class="brand"><div class="brand__mark"></div><div class="brand__name">brightvale energy</div></div>
  <h2 class="section-title-top">WHY CHOOSE US?</h2>

  <div class="worker-photo" role="img" aria-label="Installer in a hard hat fitting a solar panel on a roof"></div>
  <div class="benefits">
    <div class="benefit" style="left:45px;top:17px"><span class="benefit__mark"></span>No financing</div>
    <div class="benefit" style="left:45px;top:51px"><span class="benefit__mark"></span>No liens</div>
    <div class="benefit" style="left:45px;top:85px"><span class="benefit__mark"></span>No down payment</div>
    <div class="benefit" style="left:229px;top:17px"><span class="benefit__mark"></span>No insurance costs</div>
    <div class="benefit" style="left:229px;top:51px"><span class="benefit__mark"></span>No long-term commitment</div>
    <div class="benefit" style="left:229px;top:85px"><span class="benefit__mark"></span>No maintenance costs</div>
    <div class="benefit-rule" style="left:45px;top:43px;width:378px"></div>
    <div class="benefit-rule" style="left:45px;top:77px;width:378px"></div>
  </div>

  <div class="service-panel"></div>
  <h2 class="service-title">OUR BEST SERVICE</h2>

  <div class="service service--left" style="left:73px;top:470px">
    <svg class="service__icon" viewBox="0 0 22 24" aria-hidden="true"><rect x="2" y="6" width="18" height="14" rx="2" fill="none" stroke="#b2d235" stroke-width="1.6"/><rect x="12" y="11" width="8" height="5" fill="none" stroke="#b2d235" stroke-width="1.6"/></svg>
    <div class="service__name">Affordable &amp; Transparent:</div>
    <p class="service__text">Simple pricing, no hidden fees and a fixed monthly rate lower than typical energy bills.</p>
  </div>
  <div class="service service--left" style="left:73px;top:549px">
    <svg class="service__icon" viewBox="0 0 22 24" aria-hidden="true"><path d="M8 2v5h6V2M11 7v6" fill="none" stroke="#b2d235" stroke-width="2"/><rect x="6" y="13" width="10" height="10" rx="3" fill="none" stroke="#b2d235" stroke-width="1.6"/></svg>
    <div class="service__name">Expert Installation:</div>
    <p class="service__text">Certified professionals handle installation, maintenance, and repairs end to end.</p>
  </div>
  <div class="service service--right" style="left:308px;top:470px">
    <svg class="service__icon" viewBox="0 0 22 24" aria-hidden="true"><path d="M11 22s7-8 7-13a7 7 0 0 0-14 0c0 5 7 13 7 13z" fill="none" stroke="#b2d235" stroke-width="1.6"/><circle cx="11" cy="9" r="2.5" fill="none" stroke="#b2d235" stroke-width="1.6"/></svg>
    <div class="service__name">Local Expertise:</div>
    <p class="service__text">Florida-based team that understands the needs of Orlando and statewide homeowners.</p>
  </div>
  <div class="service service--right" style="left:308px;top:549px">
    <svg class="service__icon" viewBox="0 0 22 24" aria-hidden="true"><path d="M11 2c6 5 7 12 0 17C4 14 5 7 11 2zM11 10v13" fill="none" stroke="#b2d235" stroke-width="1.6"/></svg>
    <div class="service__name">Eco-Friendly:</div>
    <p class="service__text">Clean, renewable solar energy that helps reduce your carbon footprint.</p>
  </div>

  <div class="back-footer"></div>
  <p class="cta">Get Started Today!</p>
  <p class="contact-line">Phone: (555) 014-2290<span>|</span>Address: 48 Sample Ave., Any City<span>|</span>Website: www.brightvaleenergy.com</p>
</section>

</body>
</html>
```